Kestrelmoor Advisory Services LLC
The Quiet Hand Consutants
Project: Kestrelmoor Advisory Services LLC
Kestrelmoor Advisory Services LLC - Financial Services
Creative Brief
Professional
Warrick Dunstan Hollowell
Senior Managing Director
388 West 19th Street New York, N.T. 10024
whollowell@kmaservices.net
KESTRELMOORADVISORYSERVICES.COM

```html
<!DOCTYPE html>
<html lang="en">
<head>
<meta charset="utf-8">
<title>Kestrelmoor Advisory Services – Business Card</title>
<link rel="stylesheet" href="https://fonts.googleapis.com/css2?family=Cinzel:wght@600&family=Arimo:wght@400;700&display=swap">
<style>
  :root {
    --backdrop: #7a4f2c;
    --card-white: #ffffff;
    --brand-blue: #1b5fae;
    --deep-blue: #0d3f86;
    --light-blue: #5fa8e6;
    --gold: #c9a247;
    --ink: #1d1d1d;
    --ink-soft: #3c3c3c;
  }
  * { box-sizing: border-box; margin: 0; padding: 0; }
  html, body { width: 1200px; height: 367px; overflow: hidden; }
  body {
    background: var(--backdrop);
    font-family: "Arimo", Arial, sans-serif;
    color: var(--ink);
    position: relative;
  }
  .card {
    position: absolute;
    top: 34px;
    width: 544px;
    height: 304px;
    border-radius: 14px;
    overflow: hidden;
    background: var(--card-white);
    box-shadow: 0 3px 8px rgba(0,0,0,.35);
  }
  .card--front { left: 28px; }
  .card--back { left: 626px; }
  .card__bg { position: absolute; inset: 0; width: 100%; height: 100%; }

  .brand {
    position: absolute;
    left: 0; right: 0;
    display: flex;
    align-items: center;
    justify-content: center;
    gap: 10px;
  }
  .brand__dot { width: 14px; height: 14px; border-radius: 50%; background: var(--gold); flex: none; }
  .brand__name {
    font-family: "Cinzel", "Times New Roman", serif;
    font-weight: 600;
    color: var(--brand-blue);
    text-align: center;
    line-height: 1.05;
    letter-spacing: .5px;
  }
  .card--front .brand { top: 58px; }
  .card--front .brand__name { font-size: 22px; }
  .card--back .brand { top: 140px; }
  .card--back .brand__name { font-size: 38px; }

  .person { position: absolute; left: 64px; top: 154px; display: flex; align-items: baseline; gap: 14px; }
  .person__name { font-weight: 700; font-size: 17px; }
  .person__title { font-size: 12.5px; color: var(--ink-soft); }

  .contacts { position: absolute; top: 200px; font-size: 12px; line-height: 19px; color: var(--ink); }
  .contacts--main { left: 46px; }
  .contacts--side { left: 376px; }
  .contacts dt { display: inline-block; width: 22px; color: var(--brand-blue); }
  .contacts dd { display: inline; }
  .contacts .row { display: block; }
  .address { margin-top: 19px; }

  .web { position: absolute; left: 0; right: 0; bottom: 22px; text-align: center; font-size: 13px; color: var(--ink); }
</style>
</head>
<body>

<section class="card card--front" aria-label="Business card front">
  <svg class="card__bg" viewBox="0 0 544 304" preserveAspectRatio="none" aria-hidden="true">
    <defs>
      <linearGradient id="frontBand" x1="0" y1="0" x2="1" y2="0">
        <stop offset="0" stop-color="#dfeefb"/>
        <stop offset=".45" stop-color="#8ec3ee"/>
        <stop offset="1" stop-color="#1b5fae"/>
      </linearGradient>
    </defs>
    <path d="M0 196 C140 176 300 196 544 178 L544 304 L0 304 Z" fill="url(#frontBand)"/>
    <path d="M0 262 C170 240 360 282 544 250 L544 304 L0 304 Z" fill="#0d3f86" opacity=".85"/>
    <path d="M0 188 C150 168 320 190 544 170" fill="none" stroke="#1b5fae" stroke-width="2"/>
  </svg>

  <div class="brand">
    <span class="brand__dot"></span>
    <span class="brand__name">Kestrelmoor<br>Advisory Services</span>
  </div>

  <div class="person">
    <span class="person__name">Warrick Dunstan Hollowell</span>
    <span class="person__title">Senior Managing Director</span>
  </div>

  <dl class="contacts contacts--main">
    <span class="row"><dt>T :</dt><dd>646-555-0142</dd></span>
    <span class="row"><dt>C :</dt><dd>201-555-0187</dd></span>
    <span class="row"><dt>E :</dt><dd>whollowell@kmaservices.net</dd></span>
    <span class="row"><dd>kestrelmooradvisoryservices.com</dd></span>
  </dl>

  <dl class="contacts contacts--side">
    <span class="row"><dt>F :</dt><dd>917-555-0163</dd></span>
    <span class="row address"><dd>412 Ridgeline Avenue</dd></span>
    <span class="row"><dd>Alder, WV 25890</dd></span>
  </dl>
</section>

<section class="card card--back" aria-label="Business card back">
  <svg class="card__bg" viewBox="0 0 544 304" preserveAspectRatio="none" aria-hidden="true">
    <defs>
      <linearGradient id="backTop" x1="0" y1="0" x2="1" y2="1">
        <stop offset="0" stop-color="#0d3f86"/>
        <stop offset=".55" stop-color="#1b5fae"/>
        <stop offset="1" stop-color="#5fa8e6"/>
      </linearGradient>
    </defs>
    <path d="M0 0 L544 0 L544 118 C380 104 220 150 0 132 Z" fill="url(#backTop)"/>
    <path d="M0 140 C220 158 380 112 544 126" fill="none" stroke="#5fa8e6" stroke-width="3"/>
  </svg>

  <div class="brand">
    <span class="brand__dot"></span>
    <span class="brand__name">Kestrelmoor<br>Advisory Services</span>
  </div>

  <p class="web">www.kestrelmooradvisoryservices.com</p>
</section>

</body>
</html>
```